Website Design

I require a website to be built around a CMS for a commercial client, an SME in the construction industry
I am happy to approach this 2 ways - either a full site redesign and build around a well known CMS by the successful candidate. Or a page template designed which I can then duplicate and use with a light CMS - I have enough coding experience to implement this myself.
I require a html/css file as the final piece of work,
Updates
Hi,
This is the site to be redesigned:
http://www.vexbornplatforms.co.uk/
As you can see it is quite dated.
The design should be quite focused on the images and photos of the products.
2 designs which were reject can be seen here:
vexbornplatforms.tundrapixel.co.uk
vexbornplatforms2.tundrapixel.co.uk
This is the clients main competitor: http://www.quillrigging.com/ - They are keen to have a site which is 'better' than this one.
Hope this info helps. The site will include a lightbox gallery to focus on products, please bare this is mind when submitting your designs.
Reason: Need a higher number of designs to take to the client.
We are happy just to accept PSD designs if you believe the budget is too low for a HTML design. Please get in touch if you require more info.
Please can you use the customers logo from the website in designs. Thanks
Reason: Need more designers!
Target Market(s)
Industrial/Construction Sector
Industry/Entity Type
Construction
Requirements
Must have
- final design must be in html

```html
<!DOCTYPE html>
<html lang="en">
<head>
<meta charset="utf-8">
<title>Vexborn Platforms Ltd</title>
<link href="https://fonts.googleapis.com/css2?family=Patrick+Hand&family=Oswald:wght@600&family=Gelasio&display=swap" rel="stylesheet">
<style>
:root{
  --page:#ececec;
  --white:#ffffff;
  --orange:#f07d17;
  --blue:#13a2da;
  --blue-dark:#0a7fb0;
  --ink:#1b1b1b;
  --body:#555555;
  --bar-top:#3a3a3a;
  --bar-bottom:#050505;
}
*{margin:0;padding:0;box-sizing:border-box}
html,body{width:1200px;height:1080px;overflow:hidden;background:var(--page)}
.stage{position:absolute;left:0;top:0;width:1024px;height:922px;transform:scale(1.171875);transform-origin:0 0;font-family:Arial,Helvetica,sans-serif}
.sheet{position:absolute;left:10px;top:20px;width:1004px;height:880px;background:var(--white);border:1px solid #d8d8d8}
.brand{position:absolute;left:30px;top:62px;display:flex;align-items:center;gap:8px}
.brand-mark{width:18px;height:18px;background:var(--ink)}
.brand-name{font-family:Gelasio,Georgia,serif;font-weight:700;font-size:30px;color:var(--ink);letter-spacing:1px}
.tagline{position:absolute;left:245px;top:72px;font-family:"Patrick Hand",cursive;font-size:27px;line-height:31px;color:var(--orange);text-transform:uppercase;letter-spacing:.5px}
.phone-icon{position:absolute;left:700px;top:26px}
.phone-number{position:absolute;left:773px;top:42px;font-size:28px;color:var(--blue)}
.main-nav{position:absolute;left:10px;top:158px;width:676px;height:40px;background:linear-gradient(var(--bar-top),var(--bar-bottom));display:flex;align-items:center;padding-left:24px}
.main-nav a,.footer-nav a{color:var(--white);text-decoration:none;text-transform:uppercase;font-size:11px}
.sep{color:var(--white);font-size:11px;margin:0 14px}
.main-nav .home-icon{margin-right:14px}
.hero-art{position:absolute;left:12px;top:200px;width:672px;height:390px;background:radial-gradient(ellipse at 50% 50%,#5a5452 0%,#8a8482 45%,rgba(255,255,255,0) 72%)}
.welcome{position:absolute;left:37px;top:252px;width:605px;height:266px;background:var(--white);box-shadow:2px 3px 8px rgba(0,0,0,.35);padding:20px 48px 0 21px;font-family:Gelasio,Georgia,serif}
.welcome h1{font-weight:400;font-size:23px;color:var(--orange);margin-bottom:10px}
.welcome p{font-size:17px;line-height:22px;color:var(--body);margin-bottom:22px}
.welcome a{color:#0a4ea8}
.tanks{position:absolute;left:31px;top:596px;width:360px;font-family:Gelasio,Georgia,serif}
.tanks h2{font-weight:400;font-size:24px;color:var(--orange);margin-bottom:8px}
.tanks p{font-size:13px;line-height:18px;color:var(--body)}
.tank-ribbon{position:absolute;left:0;top:716px;width:398px;height:32px;background:var(--blue);color:var(--white);font-family:Gelasio,Georgia,serif;font-size:16.5px;line-height:32px;padding-left:33px;text-decoration:none;white-space:nowrap;box-shadow:1px 2px 3px rgba(0,0,0,.3)}
.tank-ribbon svg{position:absolute;right:11px;top:11px}
.ribbon-fold{position:absolute;left:0;top:748px}
.tank-photos{position:absolute;left:413px;top:600px;width:254px;height:160px}
.card{position:absolute;background:var(--white);box-shadow:0 1px 4px rgba(0,0,0,.35);padding:5px}
.card .fill{width:100%;height:100%}
.fill.tank{background:linear-gradient(100deg,#6f7376,#a9adb0 55%,#c9d3da)}
.fill.bridge-a{background:linear-gradient(160deg,#9fb7cc,#6d5e52)}
.fill.bridge-b{background:linear-gradient(#4f8fc9,#8fa2a6 60%,#6c6458)}
.fill.bridge-c{background:linear-gradient(150deg,#3f7fc4,#9a8a78 60%,#8a5a3a)}
.side{position:absolute;left:686px;top:95px;width:315px;height:680px;background:var(--white);box-shadow:0 0 4px rgba(0,0,0,.3)}
.side-photo{position:absolute;left:5px;top:5px;width:305px;height:470px;background:linear-gradient(#2f6fb4,#6aa3d8 45%,#cfe2f2 85%,#ffffff)}
.side-caption{position:absolute;left:5px;top:5px;width:305px;height:78px;background:rgba(20,22,26,.85);color:var(--white);font-weight:700;font-size:16px;padding:27px 0 0 19px}
.gallery-cards{position:absolute;left:0;top:478px;width:315px;height:160px}
.gallery-btn{position:absolute;left:679px;top:724px;width:329px;height:51px;background:var(--blue);color:var(--white);font-family:Oswald,sans-serif;font-weight:600;font-size:27px;text-align:center;line-height:49px;letter-spacing:1px;text-decoration:none;border-bottom:3px solid var(--blue-dark)}
.footer{position:absolute;left:17px;top:850px;width:990px;height:42px;background:linear-gradient(var(--bar-top),var(--bar-bottom));display:flex;align-items:center;justify-content:space-between;padding:0 8px}
.footer-nav{display:flex;align-items:center}
.footer-nav a{text-transform:none}
.copyright{color:var(--white);font-size:11px}
</style>
</head>
<body>
<div class="stage">
  <div class="sheet"></div>

  <div class="brand"><span class="brand-mark"></span><span class="brand-name">VEXBORN</span></div>
  <p class="tagline">We design &amp; manufacture solutions<br>for difficult access problems.</p>

  <svg class="phone-icon" width="52" height="66" viewBox="0 0 52 66" aria-hidden="true">
    <rect x="8" y="3" width="30" height="56" rx="6" fill="#1b1b1b" transform="rotate(-12 23 31)"/>
    <rect x="12" y="11" width="22" height="38" rx="2" fill="#3c9fd6" transform="rotate(-12 23 31)"/>
  </svg>
  <p class="phone-number">01632 960 418</p>

  <nav class="main-nav">
    <svg class="home-icon" width="16" height="14" viewBox="0 0 16 14" aria-hidden="true"><path d="M8 0 16 7H13V14H10V9H6V14H3V7H0Z" fill="#fff"/></svg>
    <a href="#">Home</a><span class="sep">|</span>
    <a href="#">Services</a><span class="sep">|</span>
    <a href="#">Hoists</a><span class="sep">|</span>
    <a href="#">Examples</a><span class="sep">|</span>
    <a href="#">Fall Arescue</a><span class="sep">|</span>
    <a href="#">Contact Us</a>
  </nav>

  <div class="hero-art" role="img" aria-label="Grey paint strokes with drawing tools, cables and a ruler"></div>

  <section class="welcome">
    <h1>Welcome to Vexborn Platforms Ltd.</h1>
    <p>Vexborn Platforms Ltd was established in 1987 with its operatives having at that time 10 years experience. We are now able to boast that we have over 20 years experience in the cradle industry. working on many diverse and challenging projects throughout England, Scotland and Wales.</p>
    <p>For more details please browse the other pages or <a href="#">contact us</a> if you have any questions.</p>
  </section>

  <section class="tanks">
    <h2>Vexborn Tanks</h2>
    <p>Vexborn tanks will be pleased to quote you for your requirements.We have 20 years experience in supply and installation for both steel and concrete storage tanks.................................................</p>
  </section>
  <a class="tank-ribbon" href="#">Click here to visit our Vexborn Tank Website
    <svg width="7" height="10" viewBox="0 0 7 10" aria-hidden="true"><path d="M0 0 7 5 0 10Z" fill="#fff"/></svg>
  </a>
  <svg class="ribbon-fold" width="10" height="12" viewBox="0 0 10 12" aria-hidden="true"><path d="M0 0H10L10 12Z" fill="#0a7fb0"/></svg>

  <div class="tank-photos">
    <div class="card" style="left:4px;top:0;width:246px;height:150px;transform:rotate(2deg)"><div class="fill tank"></div></div>
    <div class="card" style="left:0;top:8px;width:250px;height:152px;transform:rotate(-1deg)"><div class="fill tank"></div></div>
    <div class="card" style="left:2px;top:10px;width:248px;height:148px"><div class="fill tank" role="img" aria-label="Photo of a curved concrete storage tank wall with access cradle cables"></div></div>
  </div>

  <aside class="side">
    <div class="side-photo" role="img" aria-label="Photo of a yellow access platform among steel frame beams against a blue sky"></div>
    <p class="side-caption">LOREM IPSUM DOLOR SIT AMET</p>
    <div class="gallery-cards">
      <div class="card" style="left:-6px;top:12px;width:110px;height:150px;transform:rotate(-6deg)"><div class="fill bridge-a" role="img" aria-label="Project photo of a concrete bridge pier"></div></div>
      <div class="card" style="left:88px;top:2px;width:122px;height:160px;transform:rotate(3deg)"><div class="fill bridge-b" role="img" aria-label="Project photo of a steel bridge span over water"></div></div>
      <div class="card" style="left:178px;top:14px;width:136px;height:150px;transform:rotate(10deg)"><div class="fill bridge-c" role="img" aria-label="Project photo of access work beneath a bridge deck"></div></div>
    </div>
  </aside>
  <a class="gallery-btn" href="#">VIEW PROJECT GALLERY</a>

  <footer class="footer">
    <nav class="footer-nav">
      <a href="#">Home</a><span class="sep">|</span>
      <a href="#">Services</a><span class="sep">|</span>
      <a href="#">Hoists</a><span class="sep">|</span>
      <a href="#">Examples</a><span class="sep">|</span>
      <a href="#">Fall Arescue</a><span class="sep">|</span>
      <a href="#">Sitemap</a><span class="sep">|</span>
      <a href="#">Contact Us</a>
    </nav>
    <p class="copyright">©2011, All Rights Reserved</p>
  </footer>
</div>
</body>
</html>
```